Presentation Brochure and Sample Box Design for Verdix Board

Verdix Board is our range of aluminium composite panel that our company supplies to the signage and shop fitting industries.
the range is divided into 3 sections: Signage Grade - Light Commercial Grade and Commercial Grade.
We require an, A4 double-sided folding brochure (swatch book) that folds 3 ways, opening once and then a second time to lay out 3 pages flat.

There should be a front and back cover.

The inside cover should be reserved with text blocks for written information about the composite panel.

The opposite page on the right when you first open the brochure should have all our Commercial Grade colours, which are the timber finishes and the 4mm black, white and metallic silver.

When the brochure is folded out a second time, showing all three inside pages flat, the two inside pages on the right (next to the inside cover with the written information) should show all our Signage Grade colours, followed by the Light Commercial Grade colours.
Each colour in each section should have the product code beneath the swatch.

This brochure should have a modern and professional feel suitable for presenting to signees, shop fitters and interiors designers.

We also require a box design to contain aluminium composite panel samples of all the colours in the range.

Please refer to the template attached for the box dimensions and layout.

The box should tie in with the brochure as a complete package with a modern and professional look suitable for presenting to shop fitters and interior designers.

Finally we require a small label sticker to be stuck on the back of each sample. On the sticker should be the Verdix Board logo, a space to put the product code for the sample colour and the phone number 1300 584 206.

To summarise, this package project includes:
1 tri-folding A4 brochure,
1 sample box package design
1 sample sticker label.

Please refer to the attachments for the Verdix Board logo in two formats - the colour swatch book and template for the sample box.
The Logo may be shown with either the original blue text or with the text in white. The blue icon colour should not change.

Target Market(s)

Signage, shop fitting and interior design

Font styles to use
Serif
Sans Serif

Requirements
Must have
• A modern, neat and professional upmarket look suitable for presenting to shop fitters and interior designers.
Nice to have
• A slick and classy look that makes you want to take home the box or brochure even if you're not interested in the product.
Should not have
• A cheap, untidy, low market look with too many colours.

```html
<!DOCTYPE html>
<html lang="en">
<head>
<meta charset="utf-8">
<title>Verdix Board – Swatch Guide Brochure</title>
<link href="https://fonts.googleapis.com/css2?family=Lato:wght@400;700;900&display=swap" rel="stylesheet">
<style>
:root{
  --navy:#2b3a7a;
  --navy-dark:#1f2c63;
  --blue:#2d8fd5;
  --photo-top:#3b86c4;
  --photo-bottom:#1f5f94;
  --paper:#f7f8fb;
  --line:#9aa0ad;
  --block:#cfd0d4;
  --bg:#e4e4e4;
  --text:#2b3a7a;
}
*{box-sizing:border-box;margin:0;padding:0}
html,body{width:1083px;height:1200px;overflow:hidden}
body{background:var(--bg);font-family:"Lato",Arial,sans-serif;color:var(--text);position:relative}

.spread{position:absolute;left:21px;width:1041px;height:493px;display:grid;grid-template-columns:repeat(3,347px);box-shadow:0 6px 14px rgba(0,0,0,.18)}
.spread.outer{top:55px}
.spread.inner{top:640px}
.panel{position:relative;background:var(--paper);overflow:hidden}
.panel + .panel{border-left:1px solid #dde0e6}

.header-band{position:absolute;top:0;left:0;width:347px;height:44px}
.brand{position:absolute;display:flex;align-items:center;gap:5px;font-weight:900;letter-spacing:1.5px;white-space:nowrap}
.brand .mark{width:9px;height:9px;background:var(--blue)}
.brand.on-navy{color:#fff;font-size:10px;top:14px}
.brand.large{color:var(--navy);font-size:17px}
.brand.large .mark{width:14px;height:14px}

.section-title{position:absolute;font-size:10.5px;font-weight:700;color:var(--navy);line-height:1.15;padding-bottom:2px;border-bottom:1px solid var(--line)}

.swatches{position:absolute;display:grid;grid-template-columns:repeat(4,var(--w));grid-auto-rows:var(--h);column-gap:var(--cg);row-gap:var(--rg)}
.sw{border:1px solid #5c6170;border-radius:4px;background:#fff;display:flex;align-items:center;justify-content:center;text-align:center;font-size:4px;font-weight:900;line-height:1.1;color:#222;text-transform:uppercase;padding-top:6px;box-shadow:0 1px 1px rgba(0,0,0,.15)}
.sw.dark{color:#fff}
.c-black{background:#121212}
.c-red{background:#e5272f}
.c-yellow{background:#ebdc2b}
.c-process{background:#1e8fcf}
.c-reflex{background:#2f3d8f}
.c-forest{background:#1e5941}
.c-heritage{background:#8b2f3c}
.c-orange{background:#ec6630}
.c-navy{background:#22325b}
.c-emerald{background:#1c9e4f}
.c-steel{background:#2a2e3b}
.c-charcoal{background:#cfccc2}
.c-msilver{background:#cdcbc3}
.c-raw{background:#c9cacd}
.c-brush{background:linear-gradient(135deg,#b9bbbf,#e0e1e3 45%,#a9abb0)}
.c-undercoat{background:#c8c9cc}
.c-copper{background:linear-gradient(135deg,#b87a4f,#d09a72,#a86c45)}
.c-gold{background:linear-gradient(135deg,#8e7630,#c2a550,#7e6828)}
.c-embossed{background:linear-gradient(135deg,#c9cbcf,#f0f0f2 50%,#b6b8bd)}
.c-diamond{background:linear-gradient(135deg,#bfc1c6,#e3e4e6 50%,#a9acb1)}
.c-rust{background:linear-gradient(135deg,#a5352a,#c04c34,#8f2c22)}
.c-golden-wattle{background:linear-gradient(100deg,#8c4a25,#b56a3a,#7c4020)}
.c-walnut{background:linear-gradient(100deg,#6e3a20,#955233,#5f321c)}
.c-allspice{background:linear-gradient(100deg,#5c3320,#7e4a30,#52301f)}
.c-wenge{background:linear-gradient(100deg,#4a3328,#6c4d3c,#3e2b22)}
.c-oak{background:linear-gradient(100deg,#c09a60,#dcbb85,#b18b52)}
.c-gum{background:linear-gradient(100deg,#7b4f36,#a07055,#6c4430)}
.c-pvdf-black{background:#1d0f0f}

.photo{position:absolute}
.contact{position:absolute;display:flex;align-items:center;gap:6px;font-size:6.5px;font-weight:700;color:var(--navy)}
.contact .icon{width:14px;height:14px;border-radius:50%;background:var(--navy);display:flex;align-items:center;justify-content:center}

.text-blocks{position:absolute;left:14px;top:238px;display:grid;grid-template-columns:152px 149px;grid-auto-rows:70px;gap:9px 9px}
.text-block{background:var(--block);border-radius:6px}
</style>
</head>
<body>

<!-- Outer spread: swatch page, back cover, front cover -->
<section class="spread outer">

  <article class="panel signage-page">
    <svg class="header-band" viewBox="0 0 347 44"><path d="M0 0H347V44H199L186 16H0Z" fill="var(--navy)"/></svg>
    <div class="brand on-navy" style="left:222px"><span class="mark"></span>VERDIX BOARD</div>
    <h2 class="section-title" style="left:29px;top:48px;width:140px">Signage Grade 3MM</h2>
    <div class="swatches" style="left:29px;top:83px;--w:65px;--h:37px;--cg:9px;--rg:11.6px">
      <div class="sw">High Gloss<br>White</div><div class="sw">High Gloss<br>White</div><div class="sw">High Gloss<br>White</div><div class="sw dark c-black">High Gloss<br>Black</div>
      <div class="sw dark c-black">High Gloss<br>Black</div><div class="sw">High Gloss<br>White</div><div class="sw c-brush">Brush<br>Silver</div><div class="sw c-raw">Raw<br>Aluminium</div>
      <div class="sw dark c-red">High Gloss<br>Red</div><div class="sw">High Gloss<br>White</div><div class="sw c-yellow">High Gloss<br>Yellow</div><div class="sw">High Gloss<br>White</div>
      <div class="sw dark c-process">High Gloss<br>Process Blue</div><div class="sw">High Gloss<br>White</div><div class="sw dark c-reflex">High Gloss<br>Reflex Blue</div><div class="sw">High Gloss<br>White</div>
      <div class="sw dark c-forest">High Gloss<br>Forest Green</div><div class="sw">High Gloss<br>White</div><div class="sw dark c-heritage">High Gloss<br>Heritage Red</div><div class="sw">High Gloss<br>White</div>
      <div class="sw dark c-orange">High Gloss<br>Orange</div><div class="sw">High Gloss<br>White</div><div class="sw dark c-navy">High Gloss<br>Navy Blue</div><div class="sw">High Gloss<br>White</div>
      <div class="sw c-charcoal">Metallic<br>Charcoal</div><div class="sw">High Gloss<br>White</div><div class="sw dark c-emerald">High Gloss<br>Emerald Green</div><div class="sw">High Gloss<br>White</div>
      <div class="sw c-msilver">Metallic<br>Silver</div><div class="sw">High Gloss<br>White</div><div class="sw dark c-steel">High Gloss<br>Steel Grey</div><div class="sw">High Gloss<br>White</div>
    </div>
    <div style="position:absolute;left:0;bottom:0;width:347px;height:14px;background:var(--navy)"></div>
  </article>

  <article class="panel back-cover">
    <svg class="photo" style="left:0;top:0" width="347" height="420" role="img" aria-label="Photograph of a blue aluminium-clad building corner against the sky">
      <defs><linearGradient id="sky" x1="0" y1="0" x2="0" y2="1"><stop offset="0" stop-color="var(--photo-top)"/><stop offset="1" stop-color="var(--photo-bottom)"/></linearGradient></defs>
      <path d="M0 0H347V411L0 209Z" fill="url(#sky)"/>
      <path d="M0 209L347 411" stroke="var(--navy)" stroke-width="3"/>
    </svg>
    <div class="brand large" style="left:27px;top:342px"><span class="mark"></span>VERDIX BOARD</div>
    <h2 style="position:absolute;left:27px;top:386px;font-size:19px;font-weight:900;color:var(--navy);border-bottom:1px solid var(--line);padding-bottom:1px">GET IN TOUCH</h2>
    <div class="contact" style="left:27px;top:422px">
      <span class="icon"><svg width="8" height="8" viewBox="0 0 24 24"><path d="M6 2l4 4-2 3c1 3 4 6 7 7l3-2 4 4-3 4C10 22 2 14 2 5z" fill="#fff"/></svg></span>1300 584 206</div>
    <div class="contact" style="left:126px;top:422px">
      <span class="icon"><svg width="8" height="8" viewBox="0 0 24 24"><path d="M12 2a7 7 0 0 0-7 7c0 5 7 13 7 13s7-8 7-13a7 7 0 0 0-7-7zm0 10a3 3 0 1 1 0-6 3 3 0 0 1 0 6z" fill="#fff"/></svg></span>14 Harbour Lane, Kelston, Australia</div>
    <div class="contact" style="left:27px;top:444px">
      <span class="icon"><svg width="8" height="8" viewBox="0 0 24 24"><path d="M2 12L22 3l-5 18-5-7z" fill="#fff"/></svg></span>info@verdixboard.com</div>
    <div class="contact" style="left:126px;top:444px">
      <span class="icon"><svg width="8" height="8" viewBox="0 0 24 24"><circle cx="12" cy="12" r="9" fill="none" stroke="#fff" stroke-width="2"/><path d="M3 12h18M12 3c4 4 4 14 0 18M12 3c-4 4-4 14 0 18" fill="none" stroke="#fff" stroke-width="1.5"/></svg></span>www.verdixboard.com</div>
  </article>

  <article class="panel front-cover">
    <svg class="photo" style="left:0;top:0" width="347" height="420" role="img" aria-label="Photograph continuing the blue aluminium-clad building facade">
      <defs><linearGradient id="sky2" x1="0" y1="0" x2="0" y2="1"><stop offset="0" stop-color="var(--photo-top)"/><stop offset="1" stop-color="var(--photo-bottom)"/></linearGradient></defs>
      <path d="M0 0H347V209L0 411Z" fill="url(#sky2)"/>
      <path d="M0 411L347 209" stroke="var(--navy)" stroke-width="3"/>
    </svg>
    <svg style="position:absolute;right:22px;top:0" width="62" height="92"><path d="M0 0H62V92L0 62Z" fill="var(--navy)"/></svg>
    <div style="position:absolute;right:30px;top:30px;color:#fff;font-size:12px">GUIDE</div>
    <div class="brand large" style="right:28px;top:395px;font-size:19px"><span class="mark"></span>VERDIX BOARD</div>
    <div style="position:absolute;right:28px;top:437px;font-size:12.5px;font-weight:700;color:var(--blue)">ALUMINIUM COMPOSITE PANEL</div>
    <svg style="position:absolute;right:0;top:400px" width="12" height="58"><path d="M12 0V58H6L0 40V18L6 0Z" fill="var(--blue)"/></svg>
  </article>
</section>

<!-- Inner spread: information page, light commercial page, commercial page -->
<section class="spread inner">

  <article class="panel info-page">
    <div style="position:absolute;left:0;top:0;width:210px;height:16px;background:var(--navy)"></div>
    <div class="photo" role="img" aria-label="Collage of photographs of aluminium composite clad buildings" style="left:0;top:8px;width:347px;height:170px;background:linear-gradient(160deg,#bfc3c8,#8e949b 55%,#c9ccd0)"></div>
    <div class="brand large" style="left:33px;top:198px;font-size:18px"><span class="mark"></span>VERDIX BOARD</div>
    <div style="position:absolute;left:222px;top:195px;border-left:1px solid var(--navy);padding-left:4px;font-size:8.5px;font-weight:700;line-height:1.1;color:var(--navy)">ALUMINIUM<br>COMPOSITE PANEL</div>
    <div class="text-blocks">
      <div class="text-block"></div><div class="text-block"></div>
      <div class="text-block"></div><div class="text-block"></div>
      <div class="text-block"></div><div class="text-block"></div>
    </div>
  </article>

  <article class="panel light-commercial-page">
    <svg class="header-band" viewBox="0 0 347 44"><path d="M0 0H347V16H330L318 44H190L178 16H0Z" fill="var(--navy)"/></svg>
    <div class="brand on-navy" style="left:200px"><span class="mark"></span>VERDIX BOARD</div>
    <h2 class="section-title" style="left:28px;top:66px;width:74px">Light Commercial<br>Grade 3MM</h2>
    <h2 class="section-title" style="left:173px;top:66px;width:123px">Light Commercial Grade<br>SPECIALTY SURFACES</h2>
    <div class="swatches" style="left:28px;top:105px;--w:62px;--h:35px;--cg:10px;--rg:7px">
      <div class="sw">High Gloss<br>White</div><div class="sw">Matte<br>White</div><div class="sw">Mirror<br>Gold</div><div class="sw c-undercoat">Undercoat</div>
      <div class="sw">High Gloss<br>White</div><div class="sw dark c-black">High Gloss<br>Black</div><div class="sw">Mirror<br>Silver</div><div class="sw c-undercoat">Undercoat</div>
      <div class="sw dark c-black">High Gloss<br>Black</div><div class="sw dark c-black">Matte<br>Black</div><div class="sw c-brush">Brush<br>Silver</div><div class="sw c-raw">Aluminium</div>
    </div>
    <h2 class="section-title" style="left:28px;top:250px;width:190px">Light Commercial Grade OVERSIZED</h2>
    <div class="swatches" style="left:28px;top:268px;--w:62px;--h:35px;--cg:10px;--rg:7px">
      <div class="sw">High Gloss<br>White</div><div class="sw">Matte<br>White</div><div class="sw dark c-copper">Brush<br>Copper</div><div class="sw dark c-gold">Brush<br>Gold</div>
    </div>
    <h2 class="section-title" style="left:28px;top:318px;width:250px">Light Commercial Grade SPECIALTY SURFACES</h2>
    <div class="swatches" style="left:28px;top:336px;--w:62px;--h:35px;--cg:10px;--rg:7px">
      <div class="sw c-embossed">Milled<br>Embossed</div><div class="sw c-raw">Raw<br>Aluminium</div><div class="sw">Mirror<br>Anthracite<br>Silver</div><div class="sw c-undercoat">Undercoat</div>
      <div class="sw c-diamond">Diamond Shape<br>Embossed</div><div class="sw c-raw">Raw<br>Aluminium</div><div class="sw c-brush">Brush<br>Stainless Steel</div><div class="sw">Stainless<br>Steel</div>
      <div class="sw dark c-rust">Textured<br>Rust</div><div class="sw c-undercoat">Undercoat</div>
    </div>
  </article>

  <article class="panel commercial-page">
    <svg class="header-band" viewBox="0 0 347 44"><path d="M0 0H347V16H166L154 44H0Z" fill="var(--navy)"/></svg>
    <div class="brand on-navy" style="left:24px"><span class="mark"></span>VERDIX BOARD</div>
    <h2 class="section-title" style="left:26px;top:84px;width:135px">Commercial Grade</h2>
    <h2 class="section-title" style="left:171px;top:82px;width:140px">Commercial Grade</h2>
    <div class="swatches" style="left:26px;top:113px;--w:63px;--h:36px;--cg:10px;--rg:7px">
      <div class="sw dark c-golden-wattle">Golden<br>Wattle</div><div class="sw">High Gloss<br>White</div><div class="sw dark c-wenge">Wenge<br>Dark</div><div class="sw">High Gloss<br>White</div>
      <div class="sw dark c-walnut">Walnut</div><div class="sw">High Gloss<br>White</div><div class="sw dark c-oak">Sorrento<br>Oak</div><div class="sw">High Gloss<br>White</div>
      <div class="sw dark c-allspice">Vintage<br>Allspice</div><div class="sw">High Gloss<br>White</div><div class="sw dark c-gum">Sydney<br>Spotted Gum</div><div class="sw">High Gloss<br>White</div>
    </div>
    <h2 class="section-title" style="left:26px;top:242px;width:195px">Commercial Grade 4MM</h2>
    <div class="swatches" style="left:26px;top:269px;--w:63px;--h:35px;--cg:10px;--rg:5px">
      <div class="sw c-msilver">PVDF Metallic<br>Silver</div><div class="sw">High Gloss<br>White</div><div class="sw dark c-pvdf-black">PVDF Metallic<br>Black</div><div class="sw c-undercoat">Undercoat</div>
      <div class="sw">High Gloss<br>White</div><div class="sw">PVDF Matte<br>White</div><div class="sw dark c-black">FEVE Semi Gloss<br>Black</div><div class="sw c-raw">FEVE Semi Gloss<br>White</div>
      <div class="sw dark c-black">High Gloss<br>Black</div><div class="sw dark c-black">PVDF Matte<br>Black</div>
    </div>
    <svg class="photo" style="left:0;top:0" width="347" height="493" role="img" aria-label="Photograph of a grey aluminium-clad building corner">
      <defs><linearGradient id="bldg" x1="0" y1="0" x2="1" y2="1"><stop offset="0" stop-color="#9aa2ab"/><stop offset="1" stop-color="#5e6670"/></linearGradient></defs>
      <path d="M120 493V410L215 374L265 356L347 405V493Z" fill="url(#bldg)"/>
    </svg>
  </article>
</section>

</body>
</html>
```